Kestrel Roofing & Restoration Business Card Design

Lookiing for a double sided business card design that will have rounded corners, will look good with Spot UV, Soft Laminate, or Gloss
Front of card should have Logo, Name and Contact Info, License numbers
Back of card should have Logo, maybe other small details

```html
<!DOCTYPE html>
<html lang="en">
<head>
<meta charset="utf-8">
<title>Kestrel Roofing &amp; Restoration – Business Card</title>
<link rel="stylesheet" href="https://fonts.googleapis.com/css2?family=Poppins:wght@600&family=Montserrat:wght@700&family=Figtree:wght@400&display=swap">
<style>
  :root {
    --page: #121212;
    --card: #1e1e1f;
    --ink: #f4f4f4;
    --accent: #1fa6dd;
    --strip: #f2f2f2;
  }
  * { margin: 0; padding: 0; box-sizing: border-box; }
  html, body { width: 1200px; height: 1059px; overflow: hidden; background: var(--page); }
  .canvas { position: relative; width: 1200px; height: 1059px; }

  .card {
    position: absolute;
    background: var(--card);
    border-radius: 20px;
    overflow: hidden;
    box-shadow: 0 14px 30px rgba(0,0,0,.55);
  }
  .card--front { left: 257px; top: 89px; width: 687px; height: 390px; }
  .card--back  { left: 254px; top: 547px; width: 693px; height: 393px; }

  .brand {
    position: absolute;
    display: flex;
    align-items: center;
    gap: 12px;
    font-family: "Poppins", sans-serif;
    font-weight: 600;
    color: var(--ink);
    text-transform: uppercase;
    line-height: 1.15;
  }
  .brand__mark { background: var(--accent); flex: none; }
  .card--front .brand { left: 36px; top: 52px; font-size: 23px; }
  .card--front .brand__mark { width: 40px; height: 40px; }
  .card--back .brand { left: 0; right: 0; top: 148px; justify-content: center; font-size: 35px; gap: 18px; }
  .card--back .brand__mark { width: 62px; height: 62px; }

  .person {
    position: absolute;
    right: 38px;
    top: 196px;
    text-align: right;
  }
  .person__name {
    font-family: "Montserrat", sans-serif;
    font-weight: 700;
    font-size: 23px;
    color: var(--accent);
    letter-spacing: .2px;
  }
  .person__title {
    font-family: "Figtree", sans-serif;
    font-size: 15.5px;
    color: var(--ink);
    margin-top: -1px;
  }
  .name-rule {
    position: absolute;
    left: 36px; top: 229px;
    width: 492px; height: 1px;
    background: var(--accent);
  }
  .side-tab {
    position: absolute;
    left: 670px; top: 200px;
    width: 17px; height: 35px;
    background: var(--accent);
  }

  .contact {
    position: absolute;
    left: 36px; top: 241px;
    font-family: "Figtree", sans-serif;
    font-size: 16px;
    color: var(--ink);
    line-height: 20px;
  }
  .contact__address { margin-bottom: 13px; }
  .contact__list { list-style: none; }
  .contact__list li { display: flex; align-items: center; gap: 7px; height: 24px; }
  .contact__list svg { width: 12px; height: 12px; flex: none; }

  .footer-strip {
    position: absolute;
    left: 0; bottom: 0;
    width: 500px; height: 7px;
    background: var(--strip);
  }
  .license {
    position: absolute;
    right: 0; bottom: 0;
    width: 200px; height: 28px;
    background: var(--accent);
    clip-path: polygon(23px 0, 100% 0, 100% 100%, 0 100%);
    font-family: "Figtree", sans-serif;
    font-size: 15.5px;
    color: #fff;
    display: flex;
    align-items: center;
    padding-left: 29px;
  }
</style>
</head>
<body>
<div class="canvas">

  <section class="card card--front">
    <div class="brand">
      <span class="brand__mark"></span>
      <span class="brand__name">Kestrel Roofing &amp;<br>Restoration</span>
    </div>

    <div class="person">
      <div class="person__name">DANIEL WHITCOMBE</div>
      <div class="person__title">Founder &amp; CEO</div>
    </div>
    <div class="name-rule"></div>
    <div class="side-tab"></div>

    <div class="contact">
      <p class="contact__address">418 Ridgeview Road<br>Maple Falls, Ohio 44721</p>
      <ul class="contact__list">
        <li>
          <svg viewBox="0 0 24 24" aria-hidden="true"><path fill="#1fa6dd" d="M6.6 10.8a15.1 15.1 0 0 0 6.6 6.6l2.2-2.2c.3-.3.7-.4 1-.2 1.1.4 2.3.6 3.6.6.6 0 1 .4 1 1V20c0 .6-.4 1-1 1A17 17 0 0 1 3 4c0-.6.4-1 1-1h3.5c.6 0 1 .4 1 1 0 1.3.2 2.5.6 3.6.1.3 0 .7-.2 1z"/></svg>
          (330) 555-0142
        </li>
        <li>
          <svg viewBox="0 0 24 24" aria-hidden="true"><rect x="2" y="5" width="20" height="14" fill="#1fa6dd"/><path d="M2 5l10 8 10-8" fill="none" stroke="#1e1e1f" stroke-width="2"/></svg>
          info@kestrelroofing.com
        </li>
        <li>
          <svg viewBox="0 0 24 24" aria-hidden="true"><circle cx="12" cy="12" r="10" fill="#1fa6dd"/><path d="M7 6c2 1 3 3 2 5s1 3 2 5M15 4c-1 2 0 3 2 4s3 2 2 4" fill="none" stroke="#1e1e1f" stroke-width="1.6"/></svg>
          www.kestrelroofing.com
        </li>
      </ul>
    </div>

    <div class="footer-strip"></div>
    <div class="license">License No: 704218</div>
  </section>

  <section class="card card--back">
    <div class="brand">
      <span class="brand__mark"></span>
      <span class="brand__name">Kestrel Roofing &amp;<br>Restoration</span>
    </div>
  </section>

</div>
</body>
</html>
```